Letters from the Quiet Lantern--Rising into Inner Command by Gerald T. Whitcombe. PhD

This design request is for a book cover. The book is about my higher self returning to earth as an ascended master and helicopter pilot and the ensuing conversations we have about the spiritual path. In the book there is a parable about a helicopter pilot searching for an ancient city of light as a metaphor for following our higher guidance..

The cover I have envisioned is a Corvin 62 helicopter flying in a huge, mountainous wilderness area surrounded by miles of sheer cliffs, unstable glaciers, and turbulent canyon rivers, approaching an ancient city hidden among the trees glowing in a beautiful, shimmering white light. It is magnificent. The idea here is something similar to the ancient city of Shangri-La in Tibet.

Please feel free to consider other concepts.
my website is www.authorgeraldwhitcombe.com

FYI: A picture that captures what I am looking fir is similar to the book "The Riddle of Velmoran: On the Trail of the Ninth Omen" by Martin Ashbury.

Thank you!!

```html
<!DOCTYPE html>
<html lang="en">
<head>
<meta charset="utf-8">
<title>Letters from the Quiet Lantern — Cover Wrap</title>
<link href="https://fonts.googleapis.com/css2?family=Great+Vibes&family=Cinzel:wght@400;500&family=Open+Sans:wght@400&display=swap" rel="stylesheet">
<style>
  :root {
    --night: #0d1a2e;
    --slate: #3a5068;
    --mist: #7d8c98;
    --ember: #b4573a;
    --glow: #e8a068;
    --forest: #1f3330;
    --ink: #ffffff;
    --blank: #ffffff;
  }
  html, body { margin: 0; padding: 0; overflow: hidden; background: var(--night); }
  .cover {
    position: relative;
    width: 1200px;
    height: 882px;
    overflow: hidden;
    color: var(--ink);
  }
  .artwork { position: absolute; inset: 0; }
  .back-copy {
    position: absolute;
    font-family: "Open Sans", sans-serif;
    font-size: 13.6px;
    line-height: 18.5px;
    text-align: justify;
    margin: 0;
  }
  .back-copy.lead { left: 51px; top: 64px; width: 494px; }
  .back-copy.second { left: 51px; top: 285px; width: 494px; }
  .back-copy.side { left: 262px; top: 421px; width: 283px; }
  .author-photo-slot {
    position: absolute; left: 53px; top: 417px; width: 175px; height: 238px;
    background: var(--blank);
  }
  .code-slot {
    position: absolute; left: 369px; top: 731px; width: 191px; height: 115px;
    background: var(--blank);
  }
  .spine-title, .spine-author {
    position: absolute;
    writing-mode: vertical-rl;
    font-family: "Cinzel", serif;
    font-size: 18px;
    letter-spacing: 0.5px;
    white-space: nowrap;
  }
  .spine-title { left: 588px; top: 112px; }
  .spine-author { left: 588px; top: 592px; font-size: 17px; }
  .front-title {
    position: absolute;
    font-family: "Great Vibes", cursive;
    font-weight: 400;
    margin: 0;
    text-shadow: 0 2px 8px rgba(0,0,0,0.45);
  }
  .front-title span { position: absolute; white-space: nowrap; }
  .title-line-1 { left: 708px; top: 212px; font-size: 72px; }
  .title-line-2 { left: 745px; top: 300px; font-size: 118px; }
  .title-line-3 { left: 790px; top: 425px; font-size: 118px; }
  .subtitle {
    position: absolute; left: 762px; top: 650px; width: 316px;
    font-family: "Cinzel", serif; font-size: 18px; text-align: center;
    padding-bottom: 3px; border-bottom: 1px solid var(--ink);
    white-space: nowrap; letter-spacing: 0.5px;
  }
  .front-author {
    position: absolute; left: 700px; top: 815px; width: 436px;
    font-family: "Cinzel", serif; font-size: 24px; font-weight: 500;
    text-align: center; white-space: nowrap; letter-spacing: 0.5px;
  }
</style>
</head>
<body>
<main class="cover">
  <svg class="artwork" width="1200" height="882" viewBox="0 0 1200 882" role="img" aria-label="Misty mountain wilderness with forested valley and an ancient glowing city, a pilot in a reflective helmet above, and a small helicopter flying low on the back cover">
    <defs>
      <linearGradient id="sky" x1="0" y1="0" x2="0" y2="1">
        <stop offset="0" stop-color="#0c1828"/>
        <stop offset="0.35" stop-color="#1c2d44"/>
        <stop offset="0.6" stop-color="#2c3e46"/>
        <stop offset="0.82" stop-color="#5a4038"/>
        <stop offset="1" stop-color="#a8553c"/>
      </linearGradient>
      <radialGradient id="pilot" cx="0.5" cy="0.5" r="0.5">
        <stop offset="0" stop-color="#9a9a90" stop-opacity="0.85"/>
        <stop offset="0.6" stop-color="#5e6a72" stop-opacity="0.5"/>
        <stop offset="1" stop-color="#2c3e54" stop-opacity="0"/>
      </radialGradient>
      <radialGradient id="cityglow" cx="0.5" cy="0.5" r="0.5">
        <stop offset="0" stop-color="#f4e6c8" stop-opacity="0.8"/>
        <stop offset="1" stop-color="#6c7a86" stop-opacity="0"/>
      </radialGradient>
      <radialGradient id="ember" cx="0.5" cy="0.5" r="0.5">
        <stop offset="0" stop-color="#d0704a" stop-opacity="0.7"/>
        <stop offset="1" stop-color="#a8553c" stop-opacity="0"/>
      </radialGradient>
      <linearGradient id="valley" x1="0" y1="0" x2="0" y2="1">
        <stop offset="0" stop-color="#2a3c3c" stop-opacity="0"/>
        <stop offset="0.5" stop-color="#1f3330" stop-opacity="0.7"/>
        <stop offset="1" stop-color="#3a2e2a" stop-opacity="0"/>
      </linearGradient>
    </defs>
    <rect width="1200" height="882" fill="url(#sky)"/>
    <rect x="0" y="330" width="1200" height="330" fill="url(#valley)"/>
    <ellipse cx="930" cy="130" rx="230" ry="170" fill="url(#pilot)"/>
    <ellipse cx="880" cy="540" rx="190" ry="110" fill="url(#cityglow)"/>
    <ellipse cx="220" cy="780" rx="260" ry="110" fill="url(#ember)"/>
    <ellipse cx="950" cy="820" rx="320" ry="100" fill="url(#ember)"/>
  </svg>

  <p class="back-copy lead">Contrary to popular belief, Lorem Ipsum is not simply random text. It has roots in a piece of classical Latin literature from 45 BC, making it over 2000 years old. Edwin Harrowgate, a Latin professor at Larchmont-Avery College in Virginia, looked up one of the more obscure Latin words, consectetur, from a Lorem Ipsum passage, and going through the cites of the word in classical literature, discovered the undoubtable source. Lorem Ipsum comes from sections 1.10.32 and 1.10.33 of "de Finibus Bonorum et Malorum" (The Extremes of Good and Evil) by Calvenus, written in 45 BC. This book is a treatise on the theory of ethics, very popular during the Renaissance. The first line of Lorem Ipsum, "Lorem ipsum dolor sit amet..", comes from a line in section 1.10.32.</p>

  <p class="back-copy second">The standard chunk of Lorem Ipsum used since the 1500s is reproduced below for those interested. Sections 1.10.32 and 1.10.33 from "de Finibus Bonorum et Malorum" by Calvenus are also reproduced in their exact original form, accompanied by English versions from the 1914 translation by H. Pellworth.</p>

  <div class="author-photo-slot"></div>

  <p class="back-copy side">The standard chunk of Lorem Ipsum used since the 1500s is reproduced below for those interested. Sections 1.10.32 and 1.10.33 from "de Finibus Bonorum et Malorum" by Calvenus are also reproduced in their exact original form, accompanied by English versions from the 1914 translation by H. Pellworth. Sections 1.10.32 and 1.10.33 from "de Finibus Bonorum et Malorum" by Calvenus are also reproduced in their exact original form, accompanied by English versions from the 1914 translation by H. Pellworth.</p>

  <div class="code-slot"></div>

  <div class="spine-title">Letters from the Quiet Lantern</div>
  <div class="spine-author">Gerald T. Whitcombe. PhD</div>

  <h1 class="front-title">
    <span class="title-line-1">Letters from the</span>
    <span class="title-line-2">Quiet</span>
    <span class="title-line-3">Lantern</span>
  </h1>
  <div class="subtitle">Rising into Inner Command</div>
  <div class="front-author">Gerald T. Whitcombe. PhD</div>
</main>
</body>
</html>
```